Bright Orbit IT company Soho london Stationary

We've just had a new logo designed on Pixel Harbor and we now need some Stationary to go with it.
We're a small IT support firm supporting Design companies in Soho London. Most of our clients work on Zorvas and a relatively creative so we want a relatively informal design on our stationary to reflect this.
We'd like to stick with the green in the logo but we're not adverse to adding another few colours to the palette.
Please see the attached file for our logo and not our website.

It Company

```html
<!DOCTYPE html>
<html lang="en">
<head>
<meta charset="utf-8">
<title>Bright Orbit – Business Card</title>
<link rel="stylesheet" href="https://fonts.googleapis.com/css2?family=Jost:wght@400;500;600&display=swap">
<style>
  :root {
    --page: #ecebe6;
    --green: #b8d432;
    --green-deep: #a9c526;
    --ink: #1f1f1f;
    --ink-soft: #3a3a3a;
    --white: #ffffff;
    --url-grey: #4a4f3a;
  }
  * { box-sizing: border-box; margin: 0; padding: 0; }
  html, body {
    width: 1200px; height: 900px; overflow: hidden;
    background: var(--page);
    font-family: "Jost", "Futura", sans-serif;
  }
  .sheet {
    width: 1200px; height: 900px;
    display: flex; align-items: center; justify-content: center; gap: 40px;
  }
  .card {
    position: relative;
    width: 560px; height: 320px;
    border-radius: 3px;
    overflow: hidden;
    box-shadow: 0 10px 28px rgba(0,0,0,0.14);
  }

  /* Back side */
  .card--back { background: var(--green); }
  .card__url {
    position: absolute; right: 30px; bottom: 26px;
    font-size: 21px; font-weight: 400; color: var(--url-grey);
    letter-spacing: 0.2px;
  }
  .card__url strong { color: var(--white); font-weight: 500; }

  /* Front side */
  .card--front { background: var(--green); }
  .card__header {
    position: absolute; left: 0; top: 0; width: 100%; height: 136px;
    background: var(--white);
    display: flex; align-items: center; justify-content: center; gap: 14px;
  }
  .brand__dot {
    width: 18px; height: 18px; border-radius: 50%;
    background: var(--green);
  }
  .brand__name {
    font-size: 54px; font-weight: 600; color: var(--green-deep);
    letter-spacing: 0.5px; line-height: 1;
  }
  .card__rule {
    position: absolute; left: 0; top: 139px; width: 100%; height: 4px;
    background: var(--ink);
  }
  .card__body {
    position: absolute; left: 0; top: 143px; width: 100%; bottom: 0;
    background: var(--green);
  }
  .contact {
    position: absolute; left: 30px; top: 40px;
    color: var(--ink-soft); font-size: 16px; font-weight: 500; line-height: 1.35;
  }
  .contact__lines { margin-top: 18px; list-style: none; }
  .contact__lines li { color: var(--white); font-weight: 400; font-size: 16px; line-height: 1.4; }
  .contact__label { display: inline-block; width: 16px; font-weight: 600; }
  .person {
    position: absolute; right: 150px; top: 22px; text-align: right;
  }
  .person__name { font-size: 23px; font-weight: 500; color: var(--ink); line-height: 1.1; }
  .person__role { font-size: 15px; font-weight: 400; color: var(--ink-soft); }
</style>
</head>
<body>
  <main class="sheet">
    <section class="card card--back" aria-label="Card back">
      <p class="card__url">http://<strong>bright-orbit</strong>.co.uk</p>
    </section>

    <section class="card card--front" aria-label="Card front">
      <header class="card__header">
        <span class="brand__dot" aria-hidden="true"></span>
        <span class="brand__name">Bright Orbit</span>
      </header>
      <div class="card__rule"></div>
      <div class="card__body">
        <address class="contact" style="font-style: normal;">
          42 Larkin Row<br>London W1F 7QB
          <ul class="contact__lines">
            <li><span class="contact__label">P</span> (020) 555 0142</li>
            <li><span class="contact__label">F</span> (020) 555 0142</li>
            <li><span class="contact__label">E</span> info@bright-orbit.co.uk</li>
          </ul>
        </address>
        <div class="person">
          <p class="person__name">Your Name</p>
          <p class="person__role">Position</p>
        </div>
      </div>
    </section>
  </main>
</body>
</html>
```